Corporate Design für Softwareentwickler
Schon das erste Design hat mir sehr gut gefallen. Einige kleinere Anpassungen, die ich gerne haben wollte, wurden sehr schnell in den Entwurf aufgenommen und sehr gut umgesetzt. Insgesamt bin ich mit dem Ablauf des Projekts und dem entstanden Ergebnis sehr zufrieden. Jederzeit gerne wieder...
Zielgruppe
Wir erstellen individuelle Software nach Kundenvorgabe. Schwerpunkt dabei sind Web-Anwendungen. Die Zielgruppe sind ausschließlich Firmenkunden.
Aufgabenstellung
Ich hätte gerne ein einfaches, klares und modernes Design. Es sollte Kompetenz und Zuverlässigkeit ausstrahlen.

```html
<!DOCTYPE html>
<html lang="de">
<head>
<meta charset="utf-8">
<title>Norlen Software Development – Geschäftsausstattung</title>
<link rel="stylesheet" href="https://fonts.googleapis.com/css2?family=Open+Sans:wght@400;600&family=Arimo:wght@400;700&display=swap">
<style>
  :root {
    --navy: #0f3263;
    --sky: #1b9ad2;
    --ink: #222;
    --paper: #ffffff;
    --stage-top: #d6d6d6;
    --stage-bottom: #a9a9a9;
    --faint: #b9b9b9;
  }
  * { margin: 0; padding: 0; box-sizing: border-box; }
  html, body { width: 1100px; height: 1200px; overflow: hidden; }
  body {
    position: relative;
    font-family: "Open Sans", Arial, sans-serif;
    color: var(--ink);
    background: radial-gradient(ellipse at 50% 60%, var(--stage-top), var(--stage-bottom));
  }
  .brand-header {
    position: absolute; left: 0; top: 0; width: 1100px; height: 280px;
    background: linear-gradient(#ffffff, #f1f1f1);
    box-shadow: 0 6px 14px rgba(0,0,0,.35);
    display: flex; align-items: center; justify-content: center;
  }
  .wordmark { display: flex; align-items: center; color: var(--navy); font-family: "Open Sans", Arial, sans-serif; font-weight: 400; }
  .wordmark .dot { border: 4px solid var(--navy); border-radius: 50%; flex: none; }
  .wordmark .name { line-height: 1.05; text-transform: uppercase; }
  .wordmark--hero .dot { width: 104px; height: 104px; margin-right: 22px; }
  .wordmark--hero .name { font-size: 25px; }
  .wordmark--letter .dot { width: 38px; height: 38px; border-width: 2px; margin-right: 7px; }
  .wordmark--letter .name { font-size: 10px; }
  .wordmark--card .dot { width: 58px; height: 58px; border-width: 3px; margin-right: 10px; }
  .wordmark--card .name { font-size: 14px; }

  .sheet { position: absolute; background: var(--paper); box-shadow: 8px 10px 16px rgba(0,0,0,.35); overflow: hidden; }
  .band { position: absolute; left: 0; bottom: 0; display: block; }

  .letter { left: 68px; top: 336px; width: 567px; height: 798px; }
  .letter .wordmark { position: absolute; left: 412px; top: 72px; }
  .sender-line { position: absolute; left: 60px; top: 122px; font-size: 6px; text-decoration: underline; }
  .recipient { position: absolute; left: 66px; top: 143px; font-size: 10px; line-height: 13.5px; font-style: normal; }
  .letter-body { position: absolute; left: 66px; top: 280px; width: 425px; font-size: 9.4px; line-height: 17px; }
  .salutation { margin-bottom: 17px; }
  .closing { position: absolute; left: 66px; top: 572px; font-size: 9.6px; }
  .signature { position: absolute; left: 60px; top: 588px; width: 165px; height: 28px; background: linear-gradient(90deg, rgba(40,40,40,.12), rgba(40,40,40,.04)); border-radius: 6px; }
  .signer { position: absolute; left: 66px; top: 622px; font-size: 9.6px; }
  .footer { position: absolute; left: 157px; top: 705px; display: flex; font-size: 6.6px; line-height: 10.6px; color: var(--navy); }
  .footer .col { padding: 0 6px; border-left: 1px solid var(--navy); }
  .footer .col:first-child { border-left: none; padding-left: 0; }
  .footer strong { font-weight: 600; }

  .card { font-family: "Arimo", Arial, sans-serif; width: 368px; height: 238px; left: 677px; }
  .card--front { top: 333px; }
  .card--front .wordmark { position: absolute; left: 95px; top: 42px; }
  .card-person { position: absolute; left: 52px; top: 112px; font-size: 10px; line-height: 12px; color: var(--navy); }
  .card-person .role { font-style: italic; }
  .card-person .who { font-weight: 700; }
  .card-contact { position: absolute; left: 168px; top: 112px; font-size: 10px; line-height: 12px; color: var(--navy); }
  .card-contact .company { font-weight: 700; }
  .card-contact .legal { font-size: 7.5px; }
  .card-contact .row { display: flex; }
  .card-contact .row span:first-child { width: 42px; }
  .card--back { top: 624px; }
  .card-emblem { position: absolute; left: 139px; top: 73px; width: 78px; height: 78px; border: 4px solid var(--navy); border-radius: 50%; }
  .stage-mark { position: absolute; left: 801px; top: 933px; width: 136px; height: 136px; border: 7px solid var(--faint); border-radius: 50%; opacity: .7; }
</style>
</head>
<body>

<header class="brand-header">
  <div class="wordmark wordmark--hero">
    <span class="dot"></span>
    <span class="name">Norlen<br>Software<br>Development</span>
  </div>
</header>

<article class="sheet letter">
  <div class="wordmark wordmark--letter">
    <span class="dot"></span>
    <span class="name">Norlen<br>Software<br>Development</span>
  </div>
  <p class="sender-line">Norlen Software Development, Birkenallee 9, 36110 Weidenau</p>
  <address class="recipient">
    Firma Talveron GmbH<br>Lena Brauer<br>Lindenweg 42<br>10245 Berlin
  </address>
  <div class="letter-body">
    <p class="salutation">Sehr geehrte Damen und Herren,</p>
    <p>Lorem ipsum dolor sit amet, consetetur sadipscing elitr, sed diam nonumy eirmod tempor invidunt ut labore et dolore magna aliquyam erat, sed diam voluptua. At vero eos et accusam et justo duo dolores et ea rebum. Stet clita kasd gubergren, no sea takimata sanctus est Lorem ipsum dolor sit amet. Lorem ipsum dolor sit amet, consetetur sadipscing elitr, sed diam nonumy eirmod tempor invidunt ut labore et dolore magna aliquyam erat, sed diam voluptua. At vero eos et accusam et justo duo dolores et ea rebum. Stet clita kasd gubergren, no sea takimata sanctus est Lorem ipsum dolor sit amet.</p>
    <p>Lorem ipsum dolor sit amet, consetetur sadipscing elitr, sed diam nonumy eirmod tempor invidunt ut labore et dolore magna aliquyam erat, sed diam voluptua. At vero eos et accusam et justo duo dolores et ea rebum. Stet clita kasd gubergren, no sea takimata sanctus est Lorem ipsum dolor sit amet. Lorem ipsum dolor sit amet, consetetur sadipscing elitr, sed diam nonumy eirmod tempor invidunt ut labore et dolore magna aliquyam erat, sed diam voluptua. At vero eos et accusam et justo duo dolores et ea rebum. Stet clita kasd gubergren, no sea takimata sanctus est Lorem ipsum dolor sit amet.</p>
  </div>
  <p class="closing">Mit freundlichen Grüßen</p>
  <div class="signature" role="img" aria-label="Handschriftliche Unterschrift"></div>
  <p class="signer">Martin Hollstein</p>

  <footer class="footer">
    <div class="col">
      <strong>Anschrift:</strong><br>
      Norlen Software Development UG<br>(haftungsbeschränkt)<br>Birkenallee 9, 36110 Weidenau<br>
      Geschäftsführer: Dipl.-Ing. Jonas Reddick<br>Amtsgericht Weidenau HRB 4172
    </div>
    <div class="col">
      <strong>Kontakt:</strong><br>
      Telefon: +49 6612 480310<br>Fax: &nbsp;&nbsp;&nbsp;&nbsp;+49 6612 480311<br>
      Email: &nbsp;info@norlen-softdev.de<br>Internet: www.norlen-softdev.de
    </div>
    <div class="col">
      <strong>Bankverbindung:</strong><br>
      Bank: Weidenauer Kreisbank<br>IBAN: DE12 5300 0000 0001 2345 67<br>BIC: &nbsp;&nbsp;WKRBDEF1XXX<br>
      <strong>Finanzamt Weidenau</strong><br>USt-IdNr.: DE284615093
    </div>
  </footer>

  <svg class="band" width="567" height="16" viewBox="0 0 567 16" aria-hidden="true">
    <rect width="567" height="16" fill="var(--navy)"/>
    <polygon points="0,0 142,0 130,16 0,16" fill="var(--sky)"/>
  </svg>
</article>

<section class="sheet card card--front">
  <div class="wordmark wordmark--card">
    <span class="dot"></span>
    <span class="name">Norlen<br>Software<br>Development</span>
  </div>
  <div class="card-person">
    Dipl.-Ing.<br><span class="who">Jonas Reddick</span><br><span class="role">Geschäftsführer</span>
  </div>
  <div class="card-contact">
    <div class="company">Norlen Software Development UG</div>
    <div class="legal">(haftungsbeschränkt)</div>
    <div>Birkenallee 9</div>
    <div>36110 Weidenau</div>
    <div class="row"><span>Telefon:</span><span>+49 6612 480310</span></div>
    <div class="row"><span>Fax:</span><span>+49 6612 480311</span></div>
    <div class="row"><span>Mobil:</span><span>+49 170 512 88 40</span></div>
    <div class="row"><span>Email:</span><span>info@norlen-softdev.de</span></div>
    <div>Internet: www.norlen-softdev.de</div>
  </div>
  <svg class="band" width="368" height="17" viewBox="0 0 368 17" aria-hidden="true">
    <rect width="368" height="17" fill="var(--navy)"/>
    <polygon points="0,0 90,0 78,17 0,17" fill="var(--sky)"/>
  </svg>
</section>

<section class="sheet card card--back">
  <span class="card-emblem"></span>
  <svg class="band" width="368" height="17" viewBox="0 0 368 17" aria-hidden="true">
    <rect width="368" height="17" fill="var(--navy)"/>
    <polygon points="290,0 368,0 368,17 278,17" fill="var(--sky)"/>
  </svg>
</section>

<span class="stage-mark" aria-hidden="true"></span>

</body>
</html>
```